Business Card design for a company called Tallow Flame NI

I need a business card design for my oil fired boiler servicing company. I have a logo design already and Im just looking that incorporated into the business card design. card details; Tallow Flame NI
Oil Burner Servicing - Mid Ulster Area
Service Engineer - Owen Marsh
Mobile 07751364927
email - Tallow.Flame.NI@hearthmail.example
www.tallowflameni.example
I carry out Servicing, Commissioning, Fault Finding, Warranty Validation
Target Market(s)
home owners with oil fired central heating
Industry/Entity Type
Business
Contact Information for Business Card
Tallow Flame NI
Tell. 07751364927
Web: www.tallowflameni.example
email Tallow.Flame.NI@Hearthmail.Example
Servicing Fault Finding Commissioning Warranty Validation
Look and feel

```html
<!DOCTYPE html>
<html lang="en">
<head>
<meta charset="utf-8">
<title>Tallow Flame NI – Business Card</title>
<link rel="stylesheet" href="https://fonts.googleapis.com/css2?family=Roboto:ital,wght@0,400;0,500;0,700;1,400&display=swap">
<style>
  :root {
    --backdrop: #cccccc;
    --card: #f8f8f8;
    --brand-green: #3aa63c;
    --deep-green: #1ea43a;
    --lime: #9fd12a;
    --ink: #333333;
    --muted: #555555;
    --white: #ffffff;
  }
  * { box-sizing: border-box; margin: 0; padding: 0; }
  html, body {
    width: 1200px;
    height: 1004px;
    overflow: hidden;
    background: var(--backdrop);
    font-family: "Roboto", Arial, sans-serif;
  }
  .card {
    position: absolute;
    left: 315px;
    width: 569px;
    height: 342px;
    background: var(--card);
    overflow: hidden;
  }
  .card--front { top: 148px; }
  .card--back { top: 513px; }

  /* Front */
  .front-title {
    position: absolute;
    left: 34px;
    top: 140px;
    font-size: 35px;
    font-weight: 700;
    color: var(--brand-green);
    letter-spacing: 0.2px;
  }
  .front-tagline {
    position: absolute;
    left: 35px;
    top: 185px;
    font-size: 8.5px;
    font-weight: 500;
    color: var(--brand-green);
    letter-spacing: 1.1px;
  }
  .brand-symbol-area {
    position: absolute;
    left: 320px;
    top: 0;
    width: 249px;
    height: 342px;
    background: linear-gradient(160deg, rgba(159,209,42,0.35) 0%, rgba(58,166,60,0.55) 55%, rgba(30,164,58,0.7) 100%);
  }

  /* Back */
  .engineer-name {
    position: absolute;
    left: 35px;
    top: 58px;
    font-size: 22px;
    font-weight: 700;
    color: var(--deep-green);
  }
  .engineer-role {
    position: absolute;
    left: 35px;
    top: 87px;
    font-size: 12px;
    font-style: italic;
    color: var(--muted);
  }
  .brand-lockup {
    position: absolute;
    left: 243px;
    top: 36px;
    display: flex;
    align-items: center;
  }
  .brand-dot {
    width: 64px;
    height: 64px;
    border-radius: 50%;
    background: var(--brand-green);
    margin-right: 12px;
  }
  .brand-name {
    font-size: 28px;
    font-weight: 700;
    color: var(--brand-green);
    line-height: 1;
  }
  .brand-tagline {
    font-size: 7.5px;
    font-weight: 500;
    color: var(--brand-green);
    letter-spacing: 0.9px;
    margin-top: 6px;
  }
  .contact-list {
    position: absolute;
    left: 35px;
    top: 189px;
    list-style: none;
  }
  .contact-item {
    display: flex;
    align-items: center;
    height: 21.5px;
    font-size: 14px;
    color: var(--ink);
  }
  .contact-icon {
    width: 13px;
    height: 13px;
    margin-right: 14px;
    fill: var(--deep-green);
  }
  .wave-band {
    position: absolute;
    left: 0;
    top: 0;
  }
  .service-list {
    position: absolute;
    right: 24px;
    top: 243px;
    list-style: none;
    text-align: right;
  }
  .service-item {
    font-size: 14px;
    color: var(--white);
    line-height: 18.5px;
  }
  .service-item::after {
    content: "«";
    margin-left: 10px;
  }
</style>
</head>
<body>

<section class="card card--front" aria-label="Card front">
  <div class="front-title">Tallow Flame NI</div>
  <div class="front-tagline">OIL BURNER SERVICING - MID ULSTER AREA</div>
  <div class="brand-symbol-area" role="img" aria-label="Large brand symbol in green tones"></div>
</section>

<section class="card card--back" aria-label="Card back">
  <svg class="wave-band" width="569" height="342" viewBox="0 0 569 342" aria-hidden="true">
    <defs>
      <linearGradient id="bandGreen" x1="0" y1="0" x2="0" y2="1">
        <stop offset="0" stop-color="#6dbe3a"/>
        <stop offset="1" stop-color="#16a23a"/>
      </linearGradient>
    </defs>
    <path d="M120,265 C280,250 420,180 569,168 L569,176 C430,190 300,250 120,265 Z" fill="#8bcb45"/>
    <path d="M0,268 C180,300 360,250 569,188 L569,342 L0,342 Z" fill="url(#bandGreen)"/>
    <path d="M0,290 C150,322 300,310 569,200 L569,206 C330,300 170,338 0,305 Z" fill="var(--white)"/>
    <path d="M50,278 C170,300 270,290 330,275 C270,298 160,308 50,278 Z" fill="var(--white)"/>
  </svg>

  <div class="engineer-name">Owen Marsh</div>
  <div class="engineer-role">Service Engineer</div>

  <div class="brand-lockup">
    <div class="brand-dot"></div>
    <div>
      <div class="brand-name">Tallow Flame NI</div>
      <div class="brand-tagline">OIL BURNER SERVICING - MID ULSTER AREA</div>
    </div>
  </div>

  <ul class="contact-list">
    <li class="contact-item">
      <svg class="contact-icon" viewBox="0 0 16 16" aria-hidden="true"><path d="M1,4 C1,2 3,1 8,1 C13,1 15,2 15,4 L15,6 L11,6 L11,4 L5,4 L5,6 L1,6 Z M3,8 L6,5 L10,5 L13,8 L13,15 L3,15 Z M8,9 A2,2 0 1 0 8.01,9 Z"/></svg>
      <span>07751364927</span>
    </li>
    <li class="contact-item">
      <svg class="contact-icon" viewBox="0 0 16 16" aria-hidden="true"><path d="M8,1 A7,7 0 1 0 8.01,1 Z M8,2.5 C9.5,4 10,6 10,8 C10,10 9.5,12 8,13.5 C6.5,12 6,10 6,8 C6,6 6.5,4 8,2.5 Z M2.6,7.3 L13.4,7.3 L13.4,8.7 L2.6,8.7 Z"/></svg>
      <span>www.tallowflameni.example</span>
    </li>
    <li class="contact-item">
      <svg class="contact-icon" viewBox="0 0 16 16" aria-hidden="true"><path d="M1,3 L15,3 L15,13 L1,13 Z M2.5,4.5 L8,9 L13.5,4.5 Z M2.5,11.5 L6,8 L2.5,6 Z M13.5,11.5 L10,8 L13.5,6 Z"/></svg>
      <span>Tallow.Flame.NI@Hearthmail.Example</span>
    </li>
  </ul>

  <ul class="service-list">
    <li class="service-item">Servicing</li>
    <li class="service-item">Fault Finding</li>
    <li class="service-item">Commissioning</li>
    <li class="service-item">Warranty Validation</li>
  </ul>
</section>

</body>
</html>
```